Help me create an amazing cover for my first ebook!!

I am looking to have a modern and professional looking cover for my first ebook. It will be published through Borvex Quill Self Press and will need to follow their formatting and guidelines. I want the cover to have a modern and vibrant feel, that appeals to a millennial audience. This is a real estate book that is focused on a niche category catered to young professionals, so the idea would be to appeal to them.

Title:
The Twentysomething Playbook for Duplex Living

A Smart Property Buying Plan to Start Early, Cut Your Housing Costs (Sometimes to Zero), and Speed Up Your Path to Lasting Wealth.

Davin Osterlund

Target Market(s)

Real Estate investors, investors, millennials, young professionals, college educated, 20-40 years old.Financial freedom, finance.

Industry/Entity Type

Real Estate

Font styles to use
Sans Serif

Colors

Designer to choose colors to be used in the design.

Requirements
Must have
• Must follow the borvex quill self press format. I attached a screenshot of the details, it can also be found here: https://qsp.borvexbooks.example/en_US/help/topic/R481736025
• Must include this title:
• The Twentysomething Playbook for Duplex Living
• A Smart Property Buying Plan to Start Early, Cut Your Housing Costs (Sometimes to Zero), and Speed Up Your Path to Lasting Wealth.
• Davin Osterlund.
• I added examples of book covers I like to use as a guide, I also added some color pallette examples.
Nice to have
• Modern, clean design that's not too busy. Some sort of simple photo or illustration to incorporate in the cover along with the text would be nice.

```html
<!DOCTYPE html>
<html lang="en">
<head>
<meta charset="utf-8">
<title>The Twentysomething Playbook for Duplex Living — Davin Osterlund</title>
<link rel="stylesheet" href="https://fonts.googleapis.com/css2?family=Anton&family=Poppins:wght@600&family=Roboto:wght@500;700;900&display=swap">
<style>
  :root {
    --purple: #8a1a7e;
    --purple-dark: #6e1163;
    --magenta: #a81a99;
    --magenta-light: #c23ab3;
    --title-red: #cf2645;
    --author-red: #b8242c;
    --ink: #111111;
    --orange: #ff8a3d;
    --paper: #ffffff;
    --shade: #e3e3e3;
  }
  html, body {
    margin: 0;
    padding: 0;
    overflow: hidden;
    background: var(--paper);
  }
  .cover {
    position: relative;
    width: 750px;
    height: 1200px;
    overflow: hidden;
    background:
      radial-gradient(ellipse 70% 45% at 10% 85%, var(--shade) 0%, rgba(227,227,227,0) 70%),
      radial-gradient(ellipse 60% 40% at 85% 30%, #f1f1f1 0%, rgba(241,241,241,0) 70%),
      var(--paper);
  }
  .house-art {
    position: absolute;
    left: 22px;
    top: 40px;
    width: 706px;
    height: 280px;
    background: linear-gradient(180deg, rgba(138,26,126,0.55) 0%, rgba(194,58,179,0.18) 100%);
  }
  .series-line {
    position: absolute;
    left: 0;
    width: 750px;
    top: 362px;
    margin: 0;
    text-align: center;
    font-family: "Roboto", sans-serif;
    font-weight: 700;
    font-size: 29px;
    letter-spacing: 0.5px;
    color: var(--ink);
  }
  .main-title {
    position: absolute;
    left: 0;
    width: 750px;
    top: 408px;
    margin: 0;
    text-align: center;
    font-family: "Anton", sans-serif;
    font-weight: 400;
    font-size: 104px;
    line-height: 1;
    letter-spacing: 3px;
    color: var(--title-red);
  }
  .author {
    position: absolute;
    right: 90px;
    top: 560px;
    margin: 0;
    font-family: "Poppins", sans-serif;
    font-weight: 600;
    font-size: 48px;
    color: var(--author-red);
  }
  .badge {
    position: absolute;
    border-radius: 50%;
    display: flex;
    flex-direction: column;
    align-items: center;
    justify-content: center;
    text-align: center;
    color: #ffffff;
    font-family: "Roboto", sans-serif;
    font-weight: 500;
    box-sizing: border-box;
  }
  .badge--plan, .badge--wealth {
    width: 240px;
    height: 240px;
    background: radial-gradient(circle at 40% 35%, var(--purple) 0%, var(--purple-dark) 100%);
    font-size: 22px;
    line-height: 1.3;
    padding: 0 36px;
  }
  .badge--plan { left: 100px; top: 700px; padding-bottom: 30px; }
  .badge--wealth { left: 62px; top: 912px; }
  .badge--costs {
    left: 267px;
    top: 836px;
    width: 208px;
    height: 208px;
    background: radial-gradient(circle at 40% 35%, var(--magenta-light) 0%, var(--magenta) 100%);
    padding: 0 20px;
  }
  .badge__highlight {
    color: var(--orange);
    font-weight: 900;
    font-size: 23px;
    line-height: 1.1;
    text-transform: uppercase;
  }
  .badge__note {
    font-size: 20px;
    font-weight: 700;
    line-height: 1.2;
    margin-top: 4px;
  }
</style>
</head>
<body>
  <main class="cover">
    <div class="house-art" role="img" aria-label="Outline of a house roof with chimney and small attic window, framing the title"></div>

    <p class="series-line">THE TWENTYSOMETHING PLAYBOOK FOR</p>
    <h1 class="main-title">DUPLEX LIVING</h1>
    <p class="author">Davin Osterlund</p>

    <div class="badge badge--plan">A Smart Property Buying Plan to Start Early</div>
    <div class="badge badge--wealth">Speed Up Your Path to Lasting Wealth</div>
    <div class="badge badge--costs">
      <span class="badge__highlight">Cut Your Housing Costs</span>
      <span class="badge__note">(Sometimes to Zero)</span>
    </div>
  </main>
</body>
</html>
```